Marlow EV Brochure

We would like someone to combine the 2 attached PDFs and our Website Products into a brochure.
The contact details should be as www.marlowev-demo.com. I have attached the logo and PDFS

```html
<!DOCTYPE html>
<html lang="en">
<head>
<meta charset="utf-8">
<title>Marlow EV Brochure Cover</title>
<link href="https://fonts.googleapis.com/css2?family=Saira:wght@500;700&display=swap" rel="stylesheet">
<style>
  :root {
    --backdrop: #e9ede6;
    --paper-top: #f6f7f8;
    --paper-bottom: #e8e9ea;
    --brand-green: #66bf3a;
    --ink: #2b2b2b;
    --photo-sky: #dfe4e6;
    --photo-foliage: #6f8f4a;
  }
  * { margin: 0; padding: 0; box-sizing: border-box; }
  html, body {
    width: 1200px;
    height: 900px;
    overflow: hidden;
    background: var(--backdrop);
    font-family: "Saira", sans-serif;
  }
  .cover {
    position: absolute;
    left: 290px;
    top: 20px;
    width: 620px;
    height: 860px;
    background: linear-gradient(160deg, var(--paper-top), var(--paper-bottom));
    box-shadow: 0 10px 30px rgba(0,0,0,0.15);
  }
  .cover-art {
    position: absolute;
    left: 0;
    top: 0;
  }
  .tagline {
    font-size: 17px;
    font-weight: 500;
    letter-spacing: 2px;
    fill: var(--ink);
  }
  .brand {
    position: absolute;
    right: 50px;
    top: 630px;
    display: flex;
    flex-direction: column;
    align-items: flex-start;
    gap: 8px;
  }
  .brand-row {
    display: flex;
    align-items: center;
    gap: 12px;
    white-space: nowrap;
  }
  .brand-dot {
    width: 38px;
    height: 38px;
    border-radius: 50%;
    background: var(--brand-green);
    flex: none;
  }
  .brand-name {
    font-size: 34px;
    font-weight: 700;
    line-height: 1;
    color: var(--brand-green);
  }
  .brand-url {
    font-size: 13px;
    font-weight: 500;
    letter-spacing: 1px;
    line-height: 1.2;
    white-space: nowrap;
    color: var(--ink);
  }
</style>
</head>
<body>
  <main class="cover">
    <svg class="cover-art" width="620" height="860" viewBox="0 0 620 860">
      <defs>
        <path id="tagline-arc" d="M 230 503.2 A 200 200 0 1 1 503.2 230"/>
        <radialGradient id="photo-tone" cx="50%" cy="40%" r="60%">
          <stop offset="0%" stop-color="var(--photo-sky)"/>
          <stop offset="100%" stop-color="var(--photo-foliage)"/>
        </radialGradient>
      </defs>

      <circle class="photo" cx="330" cy="330" r="150" fill="url(#photo-tone)"
              role="img" aria-label="Photo of a driver checking her phone beside an electric car at a charging station"/>

      <path class="ring" d="M 482.2 385.4 A 162 162 0 1 1 454.1 225.9"
            fill="none" stroke="var(--brand-green)" stroke-width="26"/>
      <polygon class="ring-arrow" points="430,210 486,196 476,252" fill="var(--brand-green)"/>

      <text class="tagline">
        <textPath href="#tagline-arc" textLength="720" lengthAdjust="spacing">EVERYTHING YOU NEED TO SUPERCHARGE YOUR VEHICLE OR BUSINESS</textPath>
      </text>
    </svg>

    <div class="brand">
      <div class="brand-row">
        <span class="brand-dot"></span>
        <span class="brand-name">Marlow EV</span>
      </div>
      <p class="brand-url">www.marlowev-demo.com</p>
    </div>
  </main>
</body>
</html>
```